Verdano TxRL PowerPoint Template

Template in Powerpoint 2010 format
The template is for Verdano Management Consultants, a firm based in Calgary, Alberta, Canada. For more information on Verdano, see www.verdano-example.ca
The PowerPoint presentation will be used for yearly events called TORL (Charting Our Fieldwork) and TYRL (Charting Your Fieldwork). At these one-day conferences, Verdano shares expertise/knowledge in current oil and gas technology solutions. Topics covered include: Who are the vendors? What are their products? What are their relative strengths and weaknesses? and What trends do we see?
We intend to use the template for several years. As a result, we would like the title to be dynamic, that is, changed each year to reflect the passing of time as new events are held (for example, TYRL 2013, TYRL 2014).
Verdano conducts almost all of its business in downtown Calgary for white collar clients. Our clients are primarily upstream Oil and Gas companies. Event attendees are typically business facing IT resources or business people with IT solutions responsibilities. In otherwords, we are communicating to a corporate audience.
The presentations for TYRL and TORL are compiled by multiple teams and are then merged together. As a result, previous presentations have looked unprofessional with inconsistent graphics, logos, fonts, font sizes, colours, etc. Team members using the new PowerPoint template will require guidance (within the template) on how to use it properly to provide a common look.
An example of a powerpoint presentation for a previous TYRL event that was designed in-house is attached for your reference.
Desired master slides for new PowerPoint template:
- Overall Session - Title Slide
- Functional Area – Title slide
- Content slides, including title with content, comparison, picture with caption
- Predictions slide
- Thank you slide
Desired outcome:
- a fresh, professional looking design
- a consistent look and feel across the slide-deck
- a user-friendly template/master slides
Additional concepts that COULD be incorporated:
- upstream onshore oil and gas graphics
- technology or software
NOTE: GIF and JPG versions of the VMC logo are attached. The logo colours are Blue – Pantone 288, and Yellow – Pantone 129

```html
<!DOCTYPE html>
<html lang="en">
<head>
<meta charset="utf-8">
<title>Verdano TYRL Template – Slide Masters</title>
<link href="https://fonts.googleapis.com/css2?family=Arimo:wght@400;700&display=swap" rel="stylesheet">
<style>
:root{
  --navy:#1f3b78;
  --yellow:#f7d21c;
  --yellow-soft:#fbe57a;
  --theme-yellow:#e8b800;
  --text-gray:#7a7a7a;
  --label-blue:#3a5fa8;
  --label-orange:#e9873a;
  --chart-fill:#dfe7f6;
  --chart-border:#9aa3b3;
  --leaf-dark:#a8561a;
  --leaf-light:#e9a43d;
  --thanks-red:#e0261c;
  --canvas:#ffffff;
}
*{margin:0;padding:0;box-sizing:border-box}
html,body{width:1200px;height:1000px;overflow:hidden;background:var(--canvas)}
body{position:relative;font-family:"Arimo",Arial,sans-serif}
.slide{position:absolute;width:350px;height:262px;background:#fff;overflow:hidden;
  box-shadow:3px 4px 6px rgba(0,0,0,.35);border:1px solid #d8d8d8}
.slide-header{position:absolute;left:0;top:0;width:350px;height:70px}
.slide-title{position:absolute;left:10px;top:16px;color:#fff;font-size:15.5px;font-weight:400}
.brand{position:absolute;right:8px;top:36px;display:flex;align-items:center;gap:3px;
  color:var(--navy);font-size:9px;font-weight:700}
.brand-dot{width:6px;height:6px;border-radius:50%;background:var(--yellow)}
.footer-strip{position:absolute;left:0;bottom:0;width:100%;height:5px;
  background:linear-gradient(90deg,var(--leaf-dark),var(--leaf-light),var(--leaf-dark),var(--leaf-light))}
.footer-text{position:absolute;bottom:6px;left:0;width:100%;text-align:center;font-size:4px;color:var(--yellow)}
.page-num{position:absolute;bottom:6px;right:12px;font-size:4px;color:var(--text-gray)}
.bullets{position:absolute;list-style:none;font-size:10px;line-height:11px;color:var(--text-gray)}
.bullets li{position:relative;padding-left:12px;margin-bottom:6px}
.bullets li::before{content:"•";position:absolute;left:1px;color:var(--yellow)}
.predictions{position:absolute;left:10px;top:70px;width:300px;list-style:none;font-size:11px;line-height:12px;color:var(--text-gray)}
.predictions li{display:flex;margin-bottom:11px}
.predictions .num{flex:0 0 16px;color:var(--yellow)}
.predictions .theme{color:var(--theme-yellow)}
.photo{position:absolute;border:3px solid #fff;box-shadow:0 1px 4px rgba(0,0,0,.4)}
.chart{position:absolute;left:65px;top:67px;width:248px;height:168px;background:var(--chart-fill);border:2px solid var(--chart-border)}
.chart-vline{position:absolute;left:124px;top:0;height:100%;border-left:1px dashed #6d7689}
.chart-hline{position:absolute;top:80px;left:0;width:100%;border-top:1px dashed #6d7689}
.quad{position:absolute;font-size:6.5px;color:var(--navy)}
.vendor{position:absolute;font-size:5.5px;line-height:7px;color:#222;display:flex;align-items:center;gap:4px;white-space:nowrap}
.vendor::before{content:"";width:7px;height:7px;border-radius:50%;background:var(--yellow);border:1px solid #d9a700}
.vendor-label{background:var(--chart-fill);padding:0 1px}
.axis{position:absolute;font-size:6.5px;line-height:9px}
.axis.orange{color:var(--label-orange)}
.axis.blue{color:var(--label-blue)}
.thanks-photo{position:absolute;left:0;top:0;width:350px;height:210px;
  background:radial-gradient(ellipse at 45% 45%,#f0a531 0%,#d3761c 35%,#8c5a1d 70%,#5a4a1e 100%)}
.thanks-word{position:absolute;left:0;top:112px;width:100%;text-align:center;color:var(--thanks-red);font-size:17px;font-weight:700}
.closing-title{position:absolute;left:14px;top:217px;color:var(--label-blue);font-size:13px;font-weight:400}
.closing-date{position:absolute;left:14px;top:240px;color:var(--text-gray);font-size:8.5px}
.closing-rule{position:absolute;left:0;bottom:0;width:100%;height:3px;background:var(--navy)}
</style>
</head>
<body>

<!-- Slide: vendor quadrant -->
<section class="slide" style="left:45px;top:150px">
  <svg class="slide-header" viewBox="0 0 350 70" aria-hidden="true">
    <path d="M0 0H350V22Q200 58 0 60Z" fill="var(--navy)"/>
    <path d="M0 60Q200 58 350 22V27Q200 66 0 66Z" fill="var(--yellow)"/>
  </svg>
  <h1 class="slide-title">Financial Accounting Vendors</h1>
  <div class="brand"><span class="brand-dot"></span>Verdano</div>
  <span class="axis orange" style="left:42px;top:72px">High</span>
  <span class="axis blue" style="left:2px;top:136px;width:58px;text-align:right">Product Richness<br>&amp; Maturity<br>(Canada)</span>
  <span class="axis orange" style="left:42px;top:219px">Low</span>
  <span class="axis orange" style="left:322px;top:219px">High</span>
  <div class="chart">
    <div class="chart-vline"></div><div class="chart-hline"></div>
    <span class="quad" style="left:7px;top:9px">Stable</span>
    <span class="quad" style="right:7px;top:9px">Leaders</span>
    <span class="quad" style="left:7px;bottom:6px">Be Cautious??</span>
    <span class="quad" style="right:7px;bottom:6px">Watch For</span>
    <span class="vendor" style="left:119px;top:27px"><span class="vendor-label">Northfield (FM)</span></span>
    <span class="vendor" style="left:161px;top:39px"><span class="vendor-label">Kestrel</span></span>
    <span class="vendor" style="left:134px;top:51px"><span class="vendor-label">Halvard (LedgerOne)</span></span>
    <span class="vendor" style="left:67px;top:77px"><span class="vendor-label">Corvane (Vistaline)</span></span>
    <span class="vendor" style="left:74px;top:98px"><span class="vendor-label">Tarrow Nexus</span></span>
    <span class="vendor" style="left:27px;top:125px"><span class="vendor-label">Corvane (Packrun)</span></span>
  </div>
  <span class="axis blue" style="left:0;width:100%;text-align:center;top:236px">Vision &amp; Ability to Execute</span>
  <div class="footer-text">Management Consultants</div><div class="page-num">6</div>
  <div class="footer-strip" role="img" aria-label="Autumn leaves photo strip"></div>
</section>

<!-- Slide: predictions -->
<section class="slide" style="left:433px;top:150px">
  <svg class="slide-header" viewBox="0 0 350 70" aria-hidden="true">
    <path d="M0 0H350V22Q200 58 0 60Z" fill="var(--navy)"/>
    <path d="M0 60Q200 58 350 22V27Q200 66 0 66Z" fill="var(--yellow)"/>
  </svg>
  <h1 class="slide-title">Predictions Slide</h1>
  <div class="brand"><span class="brand-dot"></span>Verdano</div>
  <ol class="predictions">
    <li><span class="num">1.</span><span><span class="theme">Theme A -</span> Lorem ipsum dolor sit amet, consectetur adipiscing elit.</span></li>
    <li><span class="num">2.</span><span><span class="theme">Theme B -</span> Mauris semper, enim ac congue hendrerit.</span></li>
    <li><span class="num">3.</span><span><span class="theme">Theme C -</span> Lorem ipsum dolor sit amet, consectetur adipiscing elit.</span></li>
    <li><span class="num">4.</span><span><span class="theme">Theme D -</span> Mauris semper, enim ac congue hendrerit.</span></li>
    <li><span class="num">5.</span><span><span class="theme">Theme E -</span> Lorem ipsum dolor sit amet, consectetur adipiscing elit.</span></li>
  </ol>
  <div class="footer-text">Management Consultants</div><div class="page-num">7</div>
  <div class="footer-strip" role="img" aria-label="Autumn leaves photo strip"></div>
</section>

<!-- Slide: picture (tall) -->
<section class="slide" style="left:821px;top:150px">
  <svg class="slide-header" viewBox="0 0 350 70" aria-hidden="true">
    <path d="M0 0H350V22Q200 58 0 60Z" fill="var(--navy)"/>
    <path d="M0 60Q200 58 350 22V27Q200 66 0 66Z" fill="var(--yellow)"/>
  </svg>
  <h1 class="slide-title">Picture slide</h1>
  <div class="brand"><span class="brand-dot"></span>Verdano</div>
  <ul class="bullets" style="left:10px;top:68px;width:180px">
    <li>Lorem ipsum dolor sit amet, consectetur adipiscing elit.</li>
    <li>Mauris semper, enim ac congue hendrerit, orci ipsum cursus erat, in varius enim sem vel purus.</li>
    <li>Praesent lacus nibh, hendrerit nec porta ut, elementum et risus.</li>
    <li>Maecenas ultricies, mauris pretium dictum hendrerit, mi elit aliquam nisl, vitae ultricies nibh diam eu orci.</li>
  </ul>
  <div class="photo" role="img" aria-label="Industrial plant piping photo" style="left:208px;top:58px;width:124px;height:182px;background:linear-gradient(160deg,#c9cdd2,#8e959c 50%,#5d6a5e)"></div>
  <div class="footer-text">Management Consultants</div><div class="page-num">8</div>
  <div class="footer-strip" role="img" aria-label="Autumn leaves photo strip"></div>
</section>

<!-- Slide: picture (refinery night) -->
<section class="slide" style="left:46px;top:543px">
  <svg class="slide-header" viewBox="0 0 350 70" aria-hidden="true">
    <path d="M0 0H350V22Q200 58 0 60Z" fill="var(--navy)"/>
    <path d="M0 60Q200 58 350 22V27Q200 66 0 66Z" fill="var(--yellow)"/>
  </svg>
  <h1 class="slide-title">Picture slide</h1>
  <div class="brand"><span class="brand-dot"></span>Verdano</div>
  <ul class="bullets" style="left:10px;top:68px;width:172px">
    <li>Lorem ipsum dolor sit amet, consectetur adipiscing elit.</li>
    <li>Mauris semper, enim ac congue hendrerit, orci ipsum cursus erat, in varius enim sem vel purus.</li>
    <li>Praesent lacus nibh, hendrerit nec porta ut, elementum et risus.</li>
    <li>Maecenas ultricies, mauris pretium dictum hendrerit, mi elit aliquam nisl, vitae ultricies nibh diam eu orci.</li>
  </ul>
  <div class="photo" role="img" aria-label="Refinery at night reflected in water" style="left:185px;top:86px;width:158px;height:98px;background:linear-gradient(180deg,#1b2230,#3b3d42 55%,#7b6a45 65%,#1a1f28)"></div>
  <div class="footer-text">Management Consultants</div><div class="page-num">9</div>
  <div class="footer-strip" role="img" aria-label="Autumn leaves photo strip"></div>
</section>

<!-- Slide: picture (offshore) -->
<section class="slide" style="left:433px;top:543px">
  <svg class="slide-header" viewBox="0 0 350 70" aria-hidden="true">
    <path d="M0 0H350V22Q200 58 0 60Z" fill="var(--navy)"/>
    <path d="M0 60Q200 58 350 22V27Q200 66 0 66Z" fill="var(--yellow)"/>
  </svg>
  <h1 class="slide-title">Picture slide</h1>
  <div class="brand"><span class="brand-dot"></span>Verdano</div>
  <ul class="bullets" style="left:10px;top:68px;width:172px">
    <li>Lorem ipsum dolor sit amet, consectetur adipiscing elit.</li>
    <li>Mauris semper, enim ac congue hendrerit, orci ipsum cursus erat, in varius enim sem vel purus.</li>
    <li>Praesent lacus nibh, hendrerit nec porta ut, elementum et risus.</li>
    <li>Maecenas ultricies, mauris pretium dictum hendrerit, mi elit aliquam nisl, vitae ultricies nibh diam eu orci.</li>
  </ul>
  <div class="photo" role="img" aria-label="Offshore oil platform under a cloudy sky" style="left:183px;top:77px;width:158px;height:120px;background:linear-gradient(180deg,#7ea6cf,#d9e4ee 45%,#9aa3a6 62%,#2f6f9a 70%,#1f4f78)"></div>
  <div class="footer-text">Management Consultants</div><div class="page-num">10</div>
  <div class="footer-strip" role="img" aria-label="Autumn leaves photo strip"></div>
</section>

<!-- Slide: thank you -->
<section class="slide" style="left:821px;top:541px">
  <div class="thanks-photo" role="img" aria-label="Close-up of an orange maple leaf in autumn"></div>
  <div class="thanks-word">THANK YOU!</div>
  <svg style="position:absolute;left:0;top:140px" width="350" height="80" viewBox="0 0 350 80" aria-hidden="true">
    <path d="M0 66Q200 60 350 5V80H0Z" fill="#fff"/>
    <path d="M0 60Q200 56 350 0V6Q200 62 0 68Z" fill="var(--yellow)"/>
    <path d="M0 68Q200 62 350 6V12Q200 66 0 72Z" fill="var(--yellow-soft)"/>
  </svg>
  <h2 class="closing-title">QUESTIONS AND DISCUSSION</h2>
  <p class="closing-date">October 14, 2010</p>
  <div class="brand" style="top:238px;right:12px"><span class="brand-dot"></span>Verdano</div>
  <div class="closing-rule"></div>
</section>

</body>
</html>
```